Medical Flyer Design for Diabetic Retinopathy

Our company (an eye care provider in Kansas City) is seeking a high quality medical flyer design that will integrate preexisting copy that has been written to be distributed to referring physicians. The design should position our company as a modern, leading provider of eye care services to our peers in the medical community. The final product can include a front and back design.

Target Market(s)

Medical Professionals

Industry/Entity Type

Medical

Font styles to use
Sans Serif

Colors
34b8a5
33a6d7
3377b5
f79021

Requirements
Should not have
• typos

```html
<!DOCTYPE html>
<html lang="en">
<head>
<meta charset="utf-8">
<title>Diabetic Retinopathy Physician Flyer</title>
<link rel="stylesheet" href="https://fonts.googleapis.com/css2?family=Arimo:wght@400;700&family=Tinos:wght@400;700&display=swap">
<style>
  :root {
    --teal: #34b8a5;
    --sky: #33a6d7;
    --blue: #3377b5;
    --orange: #f79021;
    --mint: #dff4ee;
    --ink: #1f2a30;
    --paper: #ffffff;
  }
  * { box-sizing: border-box; margin: 0; padding: 0; }
  html, body { width: 1200px; height: 1200px; overflow: hidden; background: #eef2f3; }
  body { font-family: "Arimo", Arial, sans-serif; color: var(--ink); }
  .flyer { position: relative; width: 1200px; height: 1200px; background: var(--paper); overflow: hidden; }
  .backdrop { position: absolute; inset: 0; }
  .hero-pattern { position: absolute; left: 200px; top: 0; width: 400px; height: 260px;
    background: linear-gradient(135deg, #2b7fc0 0%, #67b7e4 55%, #dff0fa 100%); }
  .hero-photo { position: absolute; left: 60px; top: 150px; width: 230px; height: 230px; border-radius: 50%;
    background: radial-gradient(circle at 40% 45%, #d9dfe4, #8a97a3); border: 10px solid var(--orange); }
  .brand { position: absolute; display: flex; align-items: center; gap: 12px; }
  .brand-mark { width: 44px; height: 44px; background: var(--orange); }
  .brand-name { font-family: "Arimo", Arial, sans-serif; font-weight: 700; font-size: 38px; color: var(--teal); }
  .brand--hero { left: 70px; top: 396px; }
  .brand--footer { left: 780px; top: 1110px; }
  .brand--footer .brand-mark { width: 34px; height: 34px; }
  .brand--footer .brand-name { font-size: 30px; }
  .heading { font-family: "Tinos", "Times New Roman", serif; color: var(--blue); font-weight: 400; line-height: 1.15; }
  .heading--caps { text-transform: uppercase; font-size: 26px; }
  .heading--section { font-size: 28px; }
  .body-text { font-size: 16px; line-height: 1.36; }
  .intro { position: absolute; left: 40px; top: 460px; width: 550px; }
  .intro .heading { margin-bottom: 8px; }
  .facts { position: absolute; left: 0; top: 696px; width: 600px; height: 190px; background: var(--mint); padding: 14px 30px 0 40px; }
  .box-title { color: var(--sky); font-size: 17px; margin-bottom: 4px; }
  .list { list-style: none; font-size: 15.5px; line-height: 1.3; white-space: nowrap; }
  .list li::before { content: "• "; }
  .types { position: absolute; left: 40px; top: 906px; width: 550px; }
  .types .heading { margin-bottom: 10px; }
  .right-top { position: absolute; left: 700px; top: 40px; width: 470px; }
  .right-top .heading { margin-top: 12px; margin-bottom: 8px; }
  .signs-title { color: var(--sky); font-size: 16px; margin-top: 8px; }
  .signs { list-style: none; font-size: 16px; font-weight: 700; line-height: 1.36; }
  .signs li::before { content: "• "; }
  .diagram-title { position: absolute; left: 880px; top: 468px; font-weight: 700; font-size: 16px; }
  .diagram { position: absolute; left: 850px; top: 496px; width: 270px; height: 196px; }
  .diagram-art { width: 100%; height: 100%; border-radius: 50% 40% 40% 50%;
    background: radial-gradient(circle at 60% 50%, #f3c6a6, #e06a3a 60%, #b8452a); }
  .treatment-box { position: absolute; left: 720px; top: 720px; width: 480px; height: 480px; background: var(--mint); padding: 30px 40px; }
  .treatment-box .list { margin-top: 6px; font-size: 18px; }
</style>
</head>
<body>
<main class="flyer">
  <svg class="backdrop" width="1200" height="1200" viewBox="0 0 1200 1200" aria-hidden="true">
    <path d="M700 0 C620 260 560 520 640 760 C700 940 740 1080 780 1200 L720 1200 L720 720 L600 0 Z" fill="var(--teal)" opacity="0.75"/>
    <path d="M660 0 C600 280 560 540 620 760 C670 950 710 1080 740 1200" fill="none" stroke="var(--sky)" stroke-width="14"/>
  </svg>
  <div class="hero-pattern" role="img" aria-label="Blue background of molecular structure graphics"></div>
  <svg class="backdrop" width="1200" height="1200" viewBox="0 0 1200 1200" aria-hidden="true">
    <path d="M0 300 C120 240 260 250 360 260 C430 160 470 80 520 0 L560 0 C520 100 470 200 400 300 C280 290 140 280 0 340 Z" fill="var(--orange)"/>
  </svg>
  <div class="hero-photo" role="img" aria-label="Photo of a patient having an eye examination"></div>

  <div class="brand brand--hero"><span class="brand-mark"></span><span class="brand-name">Brightline Vision</span></div>

  <section class="intro">
    <h1 class="heading heading--caps">New Strategies for Diabetic Retinopathy</h1>
    <p class="body-text">Diabetic Retinopathy <b>(DR)</b> is the leading cause of blindness among working-age Americans, according to national health researchers. Yet, many cases could be prevented with regular eye exams and appropriate treatment. Federal insurers have targeted diabetic eye disease management as a focus of care and issued specific <b>quality</b> codes to report on eye disease management which can be reported by Primary Care doctors as well as Eye Care providers.</p>
  </section>

  <section class="facts">
    <h3 class="box-title">Diabetic Retinopathy Facts:</h3>
    <ul class="list">
      <li>5 million Americans age 40 and older have DR</li>
      <li>16 million will have retinopathy by 2050</li>
      <li>50% of Diabetics acquire DR within 10 years of diagnosis</li>
      <li>94% of Diabetics acquire DR within 20 years of diagnosis</li>
      <li>Only 33% of diabetics have had an exam within 1 year</li>
      <li>Only 45% of diabetics have had an exam within 2 years</li>
      <li>Between 12,000 – 24,000 new cases of blindness from DR occur each year</li>
    </ul>
  </section>

  <section class="types">
    <h2 class="heading heading--section">Types of Diabetic Eye Disease</h2>
    <p class="body-text"><b>Non-proliferative diabetic retinopathy (NPDR)</b><br>NPDR is characterized by bleeding (dot-blot hemorrhages), microaneurysms, exudate, and edema. NPDR is graded as mild, moderate or severe and may be accompanied by clinically significant macular edema that requires treatment to prevent vision loss.</p>
  </section>

  <section class="right-top">
    <p class="body-text">Proliferative diabetic retinopathy (PDR) Of the diabetic eye diseases, PDR has the greatest risk of visual loss.</p>
    <p class="signs-title">The condition is characterized by these signs:</p>
    <ul class="signs">
      <li>Development of abnormal blood vessels (neovascularization) on or adjacent to the optic nerve</li>
      <li>Vitreous hemorrhage</li>
      <li>Ischemia from decreased or blocked blood flow</li>
    </ul>
    <h2 class="heading heading--caps">Treatment of Diabetic Retinopathy</h2>
    <p class="body-text">Today, with the help of Primary Care Physicians and Endocrinologists, diabetics can maintain excellent vision through early detection and treatment. Early detection is critically important to avoid permanent damage to delicate retinal tissue. As the patient's diabetic doctor your recommendation to obtain annual eye exams is essential for proper patient compliance.</p>
  </section>

  <p class="diagram-title">Diabetic Retinopathy</p>
  <div class="diagram"><div class="diagram-art" role="img" aria-label="Labelled cross-section illustration of an eye with diabetic retinopathy"></div></div>

  <section class="treatment-box">
    <h3 class="box-title">Current Treatment Strategies include:</h3>
    <ul class="list">
      <li>Annual Dilated Eye Exams</li>
      <li>Annual Fundus Photography</li>
      <li>Ocular Coherence Tomography</li>
      <li>Fluorescein Angiography</li>
      <li>Intravitreal Anti-VEGF Injections</li>
      <li>Intravitreal Steroid Injections</li>
      <li>Laser Photocoagulation</li>
    </ul>
  </section>
  <div class="brand brand--footer"><span class="brand-mark"></span><span class="brand-name">Brightline Vision</span></div>
</main>
</body>
</html>
```